Association qui souhaite améliorer l'accès aux personnes en situation de handicap

Nous sommes une association qui a pour objectif d'améliorer l'accessibilité, augmenter l'offre des activités réalisables dans notre région touristique.
Nous souhaitons réaliser un site internet afin de pouvoir communiquer sur notre association. Nous avons déjà conçu notre flyer sur Graphivolta. Nous souhaiterions une base graphique se rapportant à celui-ci. C'est possible de tout retravailler mais nous souhaitons tout de même retrouver la charte graphique ou code couleur du flyer.
Il nous faudrait quelques pages:
- 1 page : Acceuil / Présentation (Home), Il y aurait le descriptif de l'association, avec ses objectifs à +/- moyen terme
- 1 page : Nos réalisations, celle-ci présenterait les éléments que nous avons réalisés avec des zones de textes et des images classées chronologiquement au fur et à mesure des nouveautés
- 1 page : Media, comme la précédente, mais ou on pourrait voir ou lire sur les divers médias qui parlent de nous
- 1 page : Evenements : c'est une page pour présenter divers activités que nous allons organiser
- 1 page : Contact qui indique comment nous contacter et avec la présentation des 5 ou 6 membres du comité
- 1 link donate : qui arrive sur un formulaire de donnée que l'on pourra faire évoluer sur un système de payement par la suite. Cette bannière doit se retrouver sur toutes les pages
Il est nécessaire que se design puisse être transféré sur une lecture sur téléphone mobile
Target Market(s)
Personnes en situation de handicap
Industry/Entity Type
Associatif
Coding
Coded - Design and coding required
Number of Pages Required
5+ page

```html
<!DOCTYPE html>
<html lang="fr">
<head>
<meta charset="utf-8">
<title>Open Path Association</title>
<link rel="stylesheet" href="https://fonts.googleapis.com/css2?family=Poppins:wght@400;500;600;700;800&display=swap">
<style>
:root{
  --red:#c8102e;
  --red-dark:#9e0d24;
  --ink:#1d1d22;
  --navy:#23232d;
  --grey:#6b6b72;
  --light:#e9e9ec;
  --white:#ffffff;
}
*{margin:0;padding:0;box-sizing:border-box}
html,body{width:1200px;height:4008px;overflow:hidden}
body{font-family:"Poppins",sans-serif;color:var(--ink);background:var(--white);position:relative}
.abs{position:absolute}
svg{display:block}

/* header */
.site-header{position:absolute;top:0;left:0;width:1200px;height:64px;background:var(--white);z-index:5}
.brand{position:absolute;left:88px;top:14px;display:flex;align-items:center;gap:8px;font-weight:800;font-size:17px;color:var(--red);line-height:1;text-transform:uppercase}
.brand-mark{width:18px;height:18px;background:var(--red)}
.main-nav{position:absolute;right:88px;top:14px;display:flex;align-items:center;gap:24px;font-size:13px;font-weight:600}
.main-nav a{color:var(--ink);text-decoration:none}
.main-nav a.active{color:var(--red)}
.btn-outline{border:2px solid var(--red);color:var(--red)!important;padding:8px 26px}

/* hero */
.hero-eyebrow{left:88px;top:130px;font-size:30px;font-weight:800;letter-spacing:1px}
.hero-title{left:88px;top:168px;font-size:50px;font-weight:800;line-height:56px;text-transform:uppercase}
.hero-title .cross{display:inline-block;width:44px;height:44px;background:var(--red);vertical-align:6px;margin-left:6px;position:relative}
.hero-title .cross::before,.hero-title .cross::after{content:"";position:absolute;background:var(--white)}
.hero-title .cross::before{left:18px;top:8px;width:8px;height:28px}
.hero-title .cross::after{left:8px;top:18px;width:28px;height:8px}
.hero-text{left:88px;top:288px;width:380px;font-size:14px;line-height:22px;color:var(--grey)}
.btn-red{background:var(--red);color:var(--white);font-weight:700;font-size:14px;padding:12px 28px;display:inline-block}
.hero-btn{left:88px;top:446px}

/* about */
.about-ghost{left:718px;top:1064px;font-size:110px;font-weight:800;color:var(--light);letter-spacing:4px;line-height:1}
.about-title{left:600px;top:1168px;font-size:50px;font-weight:800;line-height:1}
.about-text{left:600px;top:1236px;width:420px;font-size:14px;line-height:22px;color:var(--grey)}
.about-names{left:600px;top:1314px;width:420px;font-size:13px;line-height:20px;color:var(--grey)}
.btn-ghost{left:600px;top:1400px;border:2px solid var(--red);border-right:0;padding:10px 26px;font-size:13px;font-weight:700}

/* achievements */
.ach-title{left:88px;top:1640px;font-size:56px;font-weight:800;line-height:58px;text-transform:uppercase}
.ach-text{left:88px;top:1768px;width:380px;font-size:14px;line-height:22px;color:var(--grey)}
.ach-arrows{left:88px;top:1824px;display:flex;gap:6px}
.ach-arrows span{width:30px;height:30px;display:block}
.photo{position:absolute}

/* projects */
.proj-title{left:556px;top:2250px;font-size:40px;font-weight:800;line-height:46px;color:var(--white);text-transform:uppercase}
.proj-list{left:556px;top:2430px;width:500px;list-style:none;color:var(--white);font-size:14px;line-height:22px}
.proj-list li{padding-left:24px;position:relative;margin-bottom:12px}
.proj-list li::before{content:"";position:absolute;left:0;top:6px;width:10px;height:10px;background:var(--white)}

/* news */
.news-title{left:0;width:1200px;top:2846px;text-align:center;font-size:46px;font-weight:800;text-transform:uppercase}
.news-card{position:absolute;top:2944px;width:276px;height:380px;background:var(--white);box-shadow:0 10px 30px rgba(0,0,0,.12);border-radius:14px;overflow:hidden}
.news-card .thumb{height:210px}
.news-card .body{padding:16px 20px}
.news-date{font-size:12px;color:var(--red);font-weight:600}
.news-head{font-size:18px;font-weight:700;line-height:22px;margin:4px 0 8px}
.news-excerpt{font-size:12px;line-height:18px;color:var(--grey)}

/* footer */
.footer-brand{left:88px;top:3716px;display:flex;align-items:center;gap:10px;font-size:26px;font-weight:800;color:var(--white);text-transform:uppercase}
.footer-brand .brand-mark{width:26px;height:26px}
.footer-info{left:528px;top:3672px;width:300px;font-size:13px;line-height:20px;color:var(--white)}
.footer-contact{left:860px;top:3676px;width:220px;text-align:center;color:var(--white);font-size:15px;line-height:22px;font-weight:600}
.footer-contact .mail{color:var(--red);font-size:12px;font-weight:500}
.copyright{left:0;top:3968px;width:1200px;text-align:center;font-size:13px;color:#b9b9c2}
</style>
</head>
<body>

<!-- Header -->
<header class="site-header">
  <div class="brand"><span class="brand-mark"></span>Open Path<br>Association</div>
  <nav class="main-nav">
    <a class="active" href="#">HOME</a>
    <a href="#">OUR ACHIEVEMENTS</a>
    <a href="#">MEDIA</a>
    <a href="#">EVENTS</a>
    <a href="#">CONTACT</a>
    <a class="btn-outline" href="#">DONATE</a>
  </nav>
</header>

<!-- Hero -->
<svg class="abs" style="left:0;top:0" width="1200" height="1000" viewBox="0 0 1200 1000">
  <defs>
    <linearGradient id="grass" x1="0" y1="0" x2="1" y2="1">
      <stop offset="0" stop-color="#eef0e6"/>
      <stop offset=".5" stop-color="#a9b27b"/>
      <stop offset="1" stop-color="#4d5a2e"/>
    </linearGradient>
  </defs>
  <g role="img" aria-label="Photo: a hand brushing tall grass beside a wheelchair">
    <polygon points="440,0 1200,0 1200,700 960,960 580,560 460,560" fill="url(#grass)"/>
  </g>
  <polygon points="0,580 520,520 0,760" fill="var(--red)"/>
  <polygon points="0,760 520,520 940,980" fill="var(--red-dark)"/>
  <polygon points="480,560 980,960 560,760" fill="var(--red)"/>
  <polygon points="960,960 1200,700 1200,860" fill="var(--red)"/>
</svg>
<div class="abs hero-eyebrow">WELCOME TO</div>
<h1 class="abs hero-title">Open Path<span class="cross"></span><br>Association</h1>
<p class="abs hero-text">We are an association whose objective is to improve accessibility, increase the offer of activities that can be carried out in our tourist region.</p>
<a class="abs btn-red hero-btn" href="#">DONATE</a>

<!-- About -->
<svg class="abs" style="left:0;top:960px" width="1200" height="620" viewBox="0 0 1200 620">
  <polygon points="88,40 480,260 88,520" fill="var(--red)"/>
  <g role="img" aria-label="Photo: committee member in an orange shirt">
    <polygon points="110,70 460,260 110,490" fill="#c9a27a"/>
  </g>
  <polygon points="1200,300 1040,480 1200,600" fill="var(--red)"/>
</svg>
<div class="abs about-ghost">ABOUT</div>
<h2 class="abs about-title">OUR COMPANY</h2>
<p class="abs about-text">Friends living in the region who are committed to making the Val-Serein region as accessible as possible to people with disabilities.</p>
<p class="abs about-names">Marc Delorme - Lucie Garnier Roux<br>- Nadia Vuilleumier - Thierry Garnier Roux -<br>Hugo Marmier</p>
<a class="abs btn-ghost" href="#">READ MORE</a>

<!-- Achievements -->
<h2 class="abs ach-title">Our<br>Achievements</h2>
<p class="abs ach-text">Lorem Ipsum has been the industry's standard dummy text ever since the 1500s, when an unknown printer took a galley of type and scrambled.</p>
<div class="abs ach-arrows">
  <span style="background:var(--red)"></span><span style="background:#cfcfd4"></span>
</div>
<div class="photo" role="img" aria-label="Photo: group in red outfits at an event" style="left:560px;top:1580px;width:250px;height:320px;background:linear-gradient(160deg,#8c2a2a,#3c2a2c)"></div>
<div class="photo" role="img" aria-label="Photo: man in a red jacket at a racing event" style="left:820px;top:1580px;width:250px;height:320px;background:linear-gradient(160deg,#9aa7b4,#a3262f)"></div>
<div class="photo" role="img" aria-label="Photo: outdoor scene with people" style="left:1080px;top:1580px;width:120px;height:320px;background:linear-gradient(160deg,#7f9fb8,#c03a40)"></div>

<!-- Projects -->
<svg class="abs" style="left:0;top:1900px" width="1200" height="900" viewBox="0 0 1200 900">
  <polygon points="1200,0 1200,120 780,200" fill="var(--red-dark)"/>
  <polygon points="0,180 1200,60 1200,760 0,820" fill="var(--red)"/>
  <polygon points="1200,760 0,820 0,880" fill="var(--red-dark)"/>
  <circle cx="200" cy="460" r="300" fill="var(--white)"/>
  <g role="img" aria-label="Photo: young girl blowing a dandelion">
    <circle cx="200" cy="460" r="285" fill="#8fa39a"/>
  </g>
</svg>
<h2 class="abs proj-title">Exemples<br>concrets de projets<br>a realiser</h2>
<ul class="abs proj-list">
  <li>Adapt accessibility to certain tourist or cultural sites</li>
  <li>Advise various players in the sector tourism and culture for the reception of people with disabilities</li>
  <li>Provide interpreters for various events</li>
  <li>Creation of a platform bringing together tourist sites, accommodation and activities adapted from the Val-Serein region</li>
</ul>

<!-- News -->
<h2 class="abs news-title">News &amp; Articles</h2>
<article class="news-card" style="left:170px">
  <div class="thumb" role="img" aria-label="Photo: three smiling women" style="background:linear-gradient(160deg,#d9c3a8,#8a6a50)"></div>
  <div class="body">
    <div class="news-date">25-02-2023</div>
    <h3 class="news-head">Some event heading goes here</h3>
    <p class="news-excerpt">Lorem sollicitudin lorem bibendum auctor nisi elit consequat ipsum nec sagittis.</p>
  </div>
</article>
<article class="news-card" style="left:462px">
  <div class="thumb" role="img" aria-label="Photo: people dancing outdoors" style="background:linear-gradient(160deg,#c5d0d8,#b83240)"></div>
  <div class="body">
    <div class="news-date">25-02-2023</div>
    <h3 class="news-head">Some event heading goes here</h3>
    <p class="news-excerpt">Lorem sollicitudin lorem bibendum auctor nisi elit consequat ipsum nec sagittis.</p>
  </div>
</article>
<article class="news-card" style="left:754px">
  <div class="thumb" role="img" aria-label="Photo: two friends laughing" style="background:linear-gradient(160deg,#6b4a3e,#c0485a)"></div>
  <div class="body">
    <div class="news-date">25-02-2023</div>
    <h3 class="news-head">Some event heading goes here</h3>
    <p class="news-excerpt">Lorem sollicitudin lorem bibendum auctor nisi elit consequat ipsum nec sagittis.</p>
  </div>
</article>

<!-- Footer -->
<svg class="abs" style="left:0;top:3380px" width="1200" height="628" viewBox="0 0 1200 628">
  <polygon points="0,140 1200,0 1200,628 0,628" fill="var(--navy)"/>
  <polygon points="0,40 520,300 0,300" fill="var(--red)"/>
  <polygon points="0,300 520,300 0,220" fill="var(--red-dark)"/>
  <polygon points="1200,0 1200,160 820,130" fill="var(--red)"/>
  <line x1="0" y1="560" x2="1200" y2="560" stroke="#3a3a46" stroke-width="1"/>
  <circle cx="1150" cy="592" r="12" fill="var(--red)"/>
  <path d="M1145 595 l5-6 5 6" stroke="#fff" stroke-width="2" fill="none"/>
  <path d="M968 256 c-14 0-24 10-24 23 0 17 24 41 24 41s24-24 24-41c0-13-10-23-24-23z" fill="var(--red)"/>
  <circle cx="968" cy="279" r="8" fill="var(--navy)"/>
</svg>
<div class="abs footer-brand"><span class="brand-mark"></span>Open Path<br>Association</div>
<div class="abs footer-info">
  Cotisation annuelle de membre adhérent:<br>
  CHF 50.- / ADULTE<br>
  CHF 80.- / COUPLE<br>
  Cotisation annuelle de membre bienfaiteur:<br>
  DÈS 80.-<br>
  Pour les donations, merci d'insérer<br>
  l'annotation "don"
</div>
<div class="abs footer-contact" style="top:3724px">
  OpenPath Association<br>Chemin des Mélèzes 8<br>1899 Val-Serein<br>
  <span class="mail">info@openpath-assoc.org</span>
</div>
<div class="abs copyright">©Copyright 2022 | All Rights Reserved</div>

</body>
</html>
```